Management Consulting needing a cool business card for client acquisition and networking

We are looking for a business card that is progressive and fresh that conveys innovation, forward thinking, and confidence. The business card is for a company based in Charlotte NC called, 'MERIDOX CONSULTING GROUP LLC'. The company primarily works with banks, insurance, and brokerages to implement innovative solutions to help them streamline their operations, to more effectively manage risks, and to improve their customer relationships.

Target Market(s)

Typically meet with Chief Financial Officers, Chief Information Officers, Chief Operations Officer, Business Unit Leader. The target market are generally 40-55 years, male, white, master level education plus.

Industry/Entity Type

Progressive

Font styles to use
Serif
Other font styles liked:
• Calibri

Requirements
Should not have
• Designs that look too much like law firms or accounting companies. Too conservative

```html
<!DOCTYPE html>
<html lang="en">
<head>
<meta charset="utf-8">
<title>Meridox Consulting Group — Business Card</title>
<link rel="stylesheet" href="https://fonts.googleapis.com/css2?family=Cinzel:wght@400;500&family=Open+Sans:wght@400;500&display=swap">
<style>
  :root {
    --page: #ffffff;
    --card-deep: #0a1d86;
    --card-mid: #1128c0;
    --card-bright: #1f3cf7;
    --ink-light: #ffffff;
    --ink-muted: rgba(190, 200, 235, 0.78);
    --accent-red: #b00b16;
    --rule-dark: #0c0c14;
  }
  * { margin: 0; padding: 0; box-sizing: border-box; }
  html, body {
    width: 969px; height: 1200px; overflow: hidden;
    background: var(--page);
  }
  .sheet { position: relative; width: 969px; height: 1200px; }

  .card {
    position: absolute; left: 14px; width: 941px; height: 569px;
    background: linear-gradient(155deg, var(--card-deep) 0%, var(--card-mid) 55%, var(--card-bright) 100%);
    overflow: hidden;
  }
  .card--front { top: 14px; }
  .card--back { top: 611px; }

  .front-title {
    position: absolute; left: 0; right: 0; top: 282px;
    text-align: center;
    font-family: "Open Sans", sans-serif; font-weight: 400;
    font-size: 40px; letter-spacing: 1px;
    color: var(--ink-light);
  }

  .back-company {
    position: absolute; left: 51px; top: 139px;
    font-family: "Open Sans", sans-serif; font-weight: 500;
    font-size: 19px; letter-spacing: 0.4px;
    color: var(--ink-muted);
  }

  .holder {
    position: absolute; left: 400px; width: 561px; top: 236px;
    text-align: center;
    font-family: "Cinzel", serif; color: var(--ink-light);
  }
  .holder-name { font-size: 46px; font-weight: 400; letter-spacing: 3px; line-height: 1.1; }
  .holder-title { font-size: 18px; letter-spacing: 1.5px; margin-top: -2px; }

  .contact {
    position: absolute; top: 483px;
    font-family: "Cinzel", serif; font-size: 17px;
    color: var(--ink-light); letter-spacing: 0.5px;
    white-space: nowrap;
  }
  .contact--office { left: 56px; }
  .contact--cell { left: 360px; }
  .contact--email { left: 656px; }

  .band-red {
    position: absolute; left: 0; right: 0; top: 517px; height: 35px;
    background: var(--accent-red);
  }

  .page-rule {
    position: absolute; left: 0; right: 0; bottom: 0; height: 6px;
    background: var(--rule-dark);
  }
</style>
</head>
<body>
<main class="sheet">
  <section class="card card--front">
    <h1 class="front-title">MERIDOX CONSULTING GROUP LLC</h1>
  </section>

  <section class="card card--back">
    <p class="back-company">MERIDOX CONSULTING GROUP LLC</p>

    <div class="holder">
      <p class="holder-name">Nolan R. Vess</p>
      <p class="holder-title">PRISEDENT</p>
    </div>

    <p class="contact contact--office">O : 555-014-2290</p>
    <p class="contact contact--cell">C : 555-014-2290</p>
    <p class="contact contact--email">E : Nolan@mcg.Com</p>

    <div class="band-red"></div>
  </section>

  <div class="page-rule"></div>
</main>
</body>
</html>
```